Poster Design Project

We need a poster design for a "Karaoke Night" at a bar. Should appeal to a young crowd. Graphics should be musically themed.

Should include info:

When: July 29, 2013 from 7PM to 2AM
Where: Halvern's Pub
1/2 Off on draft beer until 9:30PM
Updates

Project Deadline Extended
Reason: Checking on copyright issues

Target Market(s)

U.S. Market ages 21 to 30, upscale and female

Industry/Entity Type

Crowd

Requirements
Must have
• Needs to be 2 by 3 aspect ratio. Must look good at 3 feet tall (render well at high resolution of 8100 by 5400).
Nice to have
• Do something create with the title "Karaoke Night".

```html
<!DOCTYPE html>
<html lang="en">
<head>
<meta charset="utf-8">
<title>Karaoke Night at Halvern's Pub</title>
<link rel="stylesheet" href="https://fonts.googleapis.com/css2?family=Bungee&family=Anton&family=Oswald:wght@300&family=Pathway+Gothic+One&display=swap">
<style>
  :root {
    --page: #ffffff;
    --night-deep: #05060f;
    --nebula: #1b2a9a;
    --nebula-glow: #3f5be0;
    --ridge: #3a3a3e;
    --white: #ffffff;
    --magenta: #ec1fd3;
    --yellow: #f4ea2a;
    --chrome: #bdbdbd;
  }
  html, body {
    margin: 0;
    width: 1200px;
    height: 1000px;
    overflow: hidden;
    background: var(--page);
  }
  .poster {
    position: absolute;
    left: 263px;
    top: 0;
    width: 675px;
    height: 1000px;
    overflow: hidden;
    background: var(--night-deep);
  }
  .sky {
    position: absolute;
    inset: 0;
    background:
      radial-gradient(ellipse 70% 28% at 45% 14%, var(--nebula-glow) 0%, var(--nebula) 40%, transparent 75%),
      radial-gradient(ellipse 60% 30% at 70% 50%, rgba(40,60,170,0.55) 0%, transparent 70%),
      linear-gradient(180deg, #0d1450 0%, #0a0e2e 40%, #0a0a14 65%, var(--ridge) 82%, #1c1c1e 100%);
  }
  .hand {
    position: absolute;
    left: 247px;
    top: 0;
    width: 155px;
    height: 210px;
    border-radius: 0 0 40px 60px;
    background: linear-gradient(180deg, #f2f2f2, #cfcfcf);
  }
  .microphone {
    position: absolute;
    left: 274px;
    top: 700px;
    width: 163px;
    height: 300px;
    border-radius: 80px 80px 0 0;
    background: linear-gradient(90deg, #8a8a8a, #f0f0f0 45%, #9a9a9a);
  }
  .type {
    position: absolute;
    inset: 0;
  }
  .title { font-family: "Bungee", sans-serif; }
  .subtitle { font-family: "Anton", sans-serif; fill: var(--magenta); }
  .date { font-family: "Oswald", sans-serif; font-weight: 300; fill: var(--yellow); }
  .offer { font-family: "Pathway Gothic One", sans-serif; fill: var(--white); }
  .hours { font-family: "Anton", sans-serif; fill: var(--magenta); }
  .rule { stroke: var(--white); stroke-width: 1.5; }
</style>
</head>
<body>
  <main class="poster">
    <div class="sky" role="img" aria-label="Starry night sky with a blue nebula above dark mountain ridges"></div>
    <div class="hand" role="img" aria-label="Illustrated hand reaching down from above"></div>
    <div class="microphone" role="img" aria-label="Illustrated chrome microphone rising from below"></div>

    <svg class="type" width="675" height="1000" viewBox="0 0 675 1000" aria-label="Karaoke night at Halvern's Pub, 29.07.2013, 7pm to 2am, half off on draft beer until 9.30pm">
      <defs>
        <pattern id="led-dots" width="9" height="9" patternUnits="userSpaceOnUse">
          <circle cx="4.5" cy="4.5" r="3.6" fill="#ffffff"/>
        </pattern>
      </defs>

      <text class="title" x="67" y="338" font-size="128" textLength="538" lengthAdjust="spacingAndGlyphs" fill="url(#led-dots)">KARAOKE</text>

      <text class="subtitle" x="72" y="420" font-size="62" textLength="527" lengthAdjust="spacingAndGlyphs">NIGHT AT HALVERN'S PUB</text>

      <line class="rule" x1="70" y1="441" x2="225" y2="441"/>
      <line class="rule" x1="70" y1="499" x2="225" y2="499"/>
      <line class="rule" x1="444" y1="441" x2="599" y2="441"/>
      <line class="rule" x1="444" y1="499" x2="599" y2="499"/>

      <text class="offer" x="77" y="481" font-size="30" textLength="143" lengthAdjust="spacingAndGlyphs">1/2 off on draft</text>
      <text class="offer" x="449" y="481" font-size="30" textLength="150" lengthAdjust="spacingAndGlyphs">beer until 9.30pm</text>

      <text class="date" x="234" y="559" font-size="140" textLength="208" lengthAdjust="spacingAndGlyphs">29.07.2013</text>

      <polygon points="264,568 443,568 354,675" fill="#ffffff"/>
      <text class="hours" x="280" y="604" font-size="24" textLength="113" lengthAdjust="spacingAndGlyphs">7pm to 2am</text>
    </svg>
  </main>
</body>
</html>
```